Hartwell Vegetable Oils Train and Bus Ads

We need to create 4 ads to run on buses, trains and at the train station. I have uploaded the specifications for King Bus, Taillight and Two Sheet.

For the King Bus, we need to target African Americans promoting the Vegetable and Coconut Oil products. I want to have the Hartwell logo, picture of all 3 vegetable oil products and the 1 coconut oil product and make some designs using an African American family. Give me some creative designs of maybe a family cooking with kids in the background playing. Open to any creative ideas.

For the Taillight, we need to target Hispanics promoting the Corn Oil product. I want to have the Hartwell logo, all 3 pictures of the corn oil product and make some designs using a Hispanic family. Give me some creative designs of maybe a family cooking with kids in the background playing. Open to any creative ideas.

For the two sheet, we need to create 2 ads: one targeting Hispanics and one targeting African Americans. Following the above same guidelines of both, but since the two sheets will be placed inside train stations, people have more time to read the ad vs driving pass a bus or train. Therefore, we can add more information. Add the following for the Hispanic two sheet ad:

The chef trusted Bright Meadow for salads, baking and frying, offering a clean crisp taste. Cholesterol free & 0g Trans Fat Per Serving.

Add the following for the African American two sheet ad:

Your cooking companion. Enjoy healthy meals with the goodness of Kettle Lane Coconut Oil. 0g Trans Fat Per Serving, Non-GMO, helps reduce the risk of heart disease.

All ads must mention:
The Most Trusted Cooking Oils in America for the last 75 years. Available at your local grocer.

Also, put in all the ads:
hwoils.com

Click the below link to access the product photos:

https://www.filevaultz.com/sh/72k9pq3mx1ab8ty/QRTXWL9pm-UZ3KdfHWBxNzCpq?dl=0

Target Market(s)

Hispanic and African Americans.

Industry/Entity Type

Cooking

Colors

Designer to choose colors to be used in the design.

Requirements
Must have
• All ads must be creative. I will pay for pixcrate images if you need to buy them. Make sure to clearly read the project description and follow the guidelines properly but make sure to provide very unique designs.
Nice to have
• Must be elegant, clean and unique. Hartwell Vegetable Oils is a very large company and the designs have to be made with superior quality.

```html
<!DOCTYPE html>
<html lang="en">
<head>
<meta charset="utf-8">
<title>Hartwell Vegetable Oils – Taillight Ad</title>
<link href="https://fonts.googleapis.com/css2?family=Oswald:wght@400;500&display=swap" rel="stylesheet">
<style>
  :root {
    --page: #e9e9e7;
    --paper: #ffffff;
    --ink: #111111;
    --gold: #c9a227;
    --gold-deep: #a8841c;
    --band: #0d0d0d;
    --photo-light: #eef0f2;
    --photo-mid: #c9b7a3;
    --produce: #7aa142;
    --bottle: #e8c94a;
  }
  html, body {
    margin: 0;
    width: 1200px;
    height: 1200px;
    overflow: hidden;
    background: var(--page);
    font-family: "Oswald", "Arial Narrow", sans-serif;
  }
  .taillight-ad {
    position: absolute;
    left: 40px;
    top: 415px;
    width: 1120px;
    height: 370px;
    background: var(--paper);
    overflow: hidden;
    box-shadow: 0 2px 10px rgba(0,0,0,.12);
  }
  .brand {
    position: absolute;
    left: 24px;
    top: 82px;
    display: flex;
    align-items: center;
    gap: 6px;
  }
  .brand-dot {
    width: 18px;
    height: 18px;
    border-radius: 50%;
    background: var(--gold);
  }
  .brand-name {
    font-size: 20px;
    font-weight: 500;
    color: var(--ink);
    letter-spacing: .3px;
    text-transform: uppercase;
  }
  .headline {
    position: absolute;
    left: 172px;
    top: 28px;
    margin: 0;
    font-weight: 500;
    font-size: 52px;
    line-height: 56px;
    color: var(--ink);
    text-transform: uppercase;
    letter-spacing: -0.5px;
    white-space: nowrap;
    transform: scaleX(.87);
    transform-origin: left top;
  }
  .tagline {
    position: absolute;
    left: 172px;
    top: 140px;
    margin: 0;
    font-size: 35px;
    line-height: 42px;
    font-weight: 400;
    text-transform: uppercase;
    color: var(--ink);
    white-space: nowrap;
    transform: scaleX(.9);
    transform-origin: left top;
  }
  .tagline .years { color: var(--gold); }
  .availability {
    position: absolute;
    left: 50px;
    top: 208px;
    margin: 0;
    font-size: 34px;
    line-height: 42px;
    font-weight: 400;
    text-transform: uppercase;
    color: var(--ink);
    white-space: nowrap;
    transform: scaleX(.87);
    transform-origin: left top;
  }
  .info-band {
    position: absolute;
    left: 0;
    top: 290px;
    width: 690px;
    height: 58px;
    background: var(--band);
  }
  .info-text {
    position: absolute;
    left: 22px;
    top: 13px;
    margin: 0;
    font-size: 21px;
    line-height: 30px;
    color: #ffffff;
    text-transform: uppercase;
    white-space: nowrap;
    transform: scaleX(.84);
    transform-origin: left top;
  }
  .info-text .url { color: var(--gold); }
  .family-photo {
    position: absolute;
    left: 690px;
    top: 0;
    width: 430px;
    height: 370px;
    background: linear-gradient(160deg, var(--photo-light) 0%, #dcd6cf 45%, var(--photo-mid) 100%);
  }
  .accent {
    position: absolute;
    left: 0;
    top: 0;
  }
  .produce {
    position: absolute;
    left: 690px;
    top: 290px;
    width: 410px;
    height: 80px;
    background: linear-gradient(90deg, var(--produce), #d9603a 50%, #e89a3c);
    opacity: .85;
  }
  .product-lineup {
    position: absolute;
    left: 478px;
    top: 152px;
    width: 196px;
    height: 130px;
    background: linear-gradient(180deg, #f3df7a 0%, var(--bottle) 55%, #c8a32c 100%);
    border-radius: 12px 12px 6px 6px;
  }
</style>
</head>
<body>
  <section class="taillight-ad">
    <div class="brand">
      <span class="brand-dot"></span>
      <span class="brand-name">Hartwell</span>
    </div>

    <h1 class="headline">The most trusted cooking<br>oils in America</h1>
    <p class="tagline">For the last <span class="years">75 years</span></p>
    <p class="availability">Available at your local grocer</p>

    <div class="info-band">
      <p class="info-text">For more information visit us- <span class="url">hwoils.com</span></p>
    </div>

    <div class="product-lineup" role="img" aria-label="Three Kettle Lane corn oil bottles in different sizes"></div>
    <div class="family-photo" role="img" aria-label="Photo of a family cooking together at a stove with pots and pans"></div>
    <svg class="accent" width="1120" height="370" viewBox="0 0 1120 370" aria-hidden="true">
      <polygon points="690,130 900,0 975,0 690,175" fill="var(--gold)"/>
      <polygon points="975,0 1000,0 690,192 690,175" fill="var(--gold-deep)"/>
    </svg>
    <div class="produce" role="img" aria-label="Fresh vegetables: broccoli, peppers, carrots and tomatoes"></div>
  </section>
</body>
</html>
```